まず、縦を想定しており、画像をメインにした構成を想定しております。

上半分は覚悟を決めた中年以上の料理にが仁王立ちしているようなイメージの写真で「店を売るという選択」or「店をゆずる決断」というキャプション

下半分はやる気に満ち溢れた若者が覚悟を持って仁王立ちしているようなイメージ
「店を買う」or「店(歴史)を引きつぐ覚悟」というキャプション

そして、下の方に計算式添付の資料にあるような表を挿入。
売却した方は結局、いくら得したのか。買った方はいくら得したのかがわかるように。あとは、「査定無料」「神奈川エリアに特化した唯一のエージェントです」を記載お願いします。最後にヴェルコハーバーズという社名と連絡先を記載。

全体的なイメージではノルヴェクや外国の広告のようにシンプルだけどもどこかデザイン性を感じるように。また、信頼性も大事なので全体的にシックだけども目を引くように。
VELKO HARBORS
ヴェルコハーバーズ
0120-471-362
www.velko-harbors-jp.example
A4
片面
青系、茶系、グレー系
• 高解像度JPG (.jpg)
• イラストレーター形式 (.ai)
キャプションの修正
【メインキャプション】大事なお店、最も高く売却いたします。
【売手側キャプション】 お店を売るという選択
【買手側キャプション】お店を買うという選択

また、各キャプションを大きめに表示をお願いします。

全体的にまとまっており、柔軟に対応頂いたため。

ありがとうござました!!

```html
<!DOCTYPE html>
<html lang="ja">
<head>
<meta charset="utf-8">
<title>ヴェルコハーバーズ｜お店を売る・お店を買う</title>
<link rel="stylesheet" href="https://fonts.googleapis.com/css2?family=Noto+Serif+JP:wght@500;700;900&family=Noto+Sans+JP:wght@400;500;700;900&display=swap">
<style>
  :root {
    --navy: #1d3556;
    --navy-deep: #142641;
    --blue-mist: #c9d7e6;
    --blue-pale: #e9eff5;
    --brown: #9a3b2c;
    --red: #b8372b;
    --beige: #efe6d8;
    --beige-pale: #f8f3ec;
    --gray-text: #4a4f57;
    --gray-line: #b9bec6;
    --gray-fill: #eceef1;
    --white: #ffffff;
  }
  * { margin: 0; padding: 0; box-sizing: border-box; }
  html, body { width: 854px; height: 1200px; overflow: hidden; background: var(--white); }
  body { font-family: "Noto Sans JP", sans-serif; color: var(--gray-text); }
  .poster { position: relative; width: 854px; height: 1200px; overflow: hidden; background: var(--white); }

  /* seller band */
  .seller-band { position: absolute; left: 0; top: 0; width: 854px; height: 420px;
    background: linear-gradient(115deg, var(--blue-mist) 0%, var(--blue-pale) 38%, var(--white) 70%); }
  .seller-photo { position: absolute; right: 0; top: 0; width: 420px; height: 420px;
    background: linear-gradient(160deg, #dfe4ea 0%, #f4f5f7 45%, #c6ccd4 100%); }

  /* buyer band */
  .buyer-band { position: absolute; left: 0; top: 420px; width: 854px; height: 360px;
    background: linear-gradient(245deg, var(--beige) 0%, var(--beige-pale) 45%, var(--white) 100%); }
  .buyer-photo { position: absolute; left: 0; top: 420px; width: 430px; height: 360px;
    background: linear-gradient(200deg, #e9e3da 0%, #f6f2ec 45%, #cfc6ba 100%); }

  .vertical { position: absolute; writing-mode: vertical-rl; white-space: nowrap; }
  .catch-main { font-family: "Noto Serif JP", serif; font-weight: 900; font-size: 50px; letter-spacing: 4px; line-height: 1; }
  .catch-sub { font-family: "Noto Serif JP", serif; font-weight: 700; font-size: 24px; letter-spacing: 3px; line-height: 1; }
  .catch-body { font-size: 12.5px; line-height: 2; letter-spacing: 1.5px; }

  .seller-catch { left: 300px; top: 36px; color: var(--navy); }
  .seller-sub { left: 356px; top: 250px; color: var(--navy); }
  .seller-body { left: 168px; top: 52px; color: var(--navy-deep); }

  .buyer-catch { left: 520px; top: 446px; color: var(--brown); }
  .buyer-sub { left: 578px; top: 630px; color: var(--brown); }
  .buyer-body { left: 626px; top: 460px; color: #3d2a22; }

  .connector { position: absolute; left: 0; top: 0; width: 854px; height: 790px; }

  /* lead */
  .free-badge { position: absolute; left: 18px; top: 792px; width: 92px; height: 84px; background: var(--red);
    color: var(--white); font-family: "Noto Serif JP", serif; font-weight: 900; font-size: 28px;
    line-height: 1.15; display: flex; align-items: center; justify-content: center; text-align: center; letter-spacing: 2px; }
  .lead-title { position: absolute; left: 128px; top: 788px; font-family: "Noto Serif JP", serif; font-weight: 900;
    font-size: 37px; color: var(--navy); letter-spacing: 1px; white-space: nowrap; }
  .lead-text { position: absolute; left: 130px; top: 842px; width: 700px; font-size: 12px; line-height: 1.6; color: var(--gray-text); }

  /* simulation tables */
  .sim { position: absolute; top: 892px; width: 392px; }
  .sim-exit { left: 22px; }
  .sim-open { left: 440px; }
  .sim-title { font-family: "Noto Serif JP", serif; font-weight: 700; font-size: 16px; color: var(--navy);
    padding: 2px 0 4px; border-bottom: 2px solid var(--navy); letter-spacing: 1px; }
  .sim-open .sim-title { color: var(--brown); border-color: var(--brown); }
  .sim table { width: 100%; border-collapse: collapse; font-size: 12.5px; }
  .sim th, .sim td { border-bottom: 1px solid var(--gray-line); padding: 0 8px; height: 27px; }
  .sim thead th { font-weight: 500; font-size: 12px; background: var(--gray-fill); color: var(--gray-text); text-align: center; }
  .sim thead th.own { background: var(--navy); color: var(--white); }
  .sim-open thead th.own { background: var(--brown); }
  .sim tbody th { text-align: left; font-weight: 500; width: 124px; color: var(--navy-deep); }
  .sim td { text-align: right; font-weight: 500; }
  .sim td.own { color: var(--navy); font-weight: 700; background: #f3f6fa; }
  .sim-open td.own { color: var(--brown); background: #faf4f0; }
  .sim tr.total th, .sim tr.total td { border-bottom: 2px solid var(--gray-text); }
  .sim-merit { margin-top: 8px; height: 36px; background: var(--navy); color: var(--white); display: flex;
    align-items: center; justify-content: center; font-family: "Noto Serif JP", serif; font-weight: 900; font-size: 20px; letter-spacing: 1px; }
  .sim-merit small { font-size: 14px; font-weight: 700; margin-left: 2px; }
  .sim-open .sim-merit { background: var(--brown); }

  /* footer */
  .footer { position: absolute; left: 0; top: 1108px; width: 854px; height: 92px; border-top: 1px solid var(--gray-line); }
  .brand { position: absolute; left: 22px; top: 10px; width: 220px; }
  .brand-note { font-size: 10px; color: var(--gray-text); line-height: 1.4; margin-bottom: 6px; }
  .brand-name { display: flex; align-items: center; gap: 8px; font-weight: 900; font-size: 19px; color: var(--navy); letter-spacing: 1px; line-height: 1.2; }
  .brand-mark { width: 15px; height: 15px; background: var(--navy); }
  .brand-kana { font-size: 10.5px; color: var(--navy); margin-top: 3px; letter-spacing: 2px; }

  .contact { position: absolute; left: 258px; top: 8px; width: 340px; }
  .contact-lead { font-size: 12.5px; font-weight: 700; color: var(--navy); display: flex; align-items: center; gap: 6px; }
  .contact-tel { font-weight: 900; font-size: 38px; color: var(--navy); letter-spacing: 1px; line-height: 1.1; }
  .contact-addr { font-size: 9.5px; line-height: 1.5; color: var(--gray-text); white-space: nowrap; }

  .web { position: absolute; left: 610px; top: 10px; width: 224px; }
  .web-lead { font-size: 12.5px; font-weight: 700; color: var(--navy); }
  .web-url { font-size: 11.5px; color: var(--navy); margin: 4px 0 6px; font-weight: 500; }
  .search { display: flex; height: 28px; border: 1.5px solid var(--navy); }
  .search-field { flex: 1; font-size: 12px; display: flex; align-items: center; padding-left: 8px; color: var(--navy-deep); }
  .search-button { width: 52px; background: var(--red); color: var(--white); font-size: 12px; font-weight: 700;
    display: flex; align-items: center; justify-content: center; }
</style>
</head>
<body>
<main class="poster">

  <section class="seller-band"></section>
  <div class="seller-photo" role="img" aria-label="腕を組んで堂々と立つ白いコックコートの年配の料理人の写真"></div>

  <section class="buyer-band"></section>
  <div class="buyer-photo" role="img" aria-label="決意を秘めて立つ白いコックコートの若い料理人の写真"></div>

  <svg class="connector" viewBox="0 0 854 790" aria-hidden="true">
    <polyline points="390,404 500,404 500,424" fill="none" stroke="#1d3556" stroke-width="1.5" stroke-dasharray="4 4"/>
    <polygon points="494,420 506,420 500,432" fill="#1d3556"/>
    <polyline points="848,436 508,436 508,770" fill="none" stroke="#b8372b" stroke-width="2"/>
  </svg>

  <h2 class="vertical catch-main seller-catch">お店を売る</h2>
  <p class="vertical catch-sub seller-sub">という選択</p>
  <p class="vertical catch-body seller-body">譲渡・解約手続から造作の売却まで、<br>すべてまるっとお任せください。<br>お店を大切に使ってくれる方へ、<br>想いと共に引き継ぎます。</p>

  <h2 class="vertical catch-main buyer-catch">お店を買う</h2>
  <p class="vertical catch-sub buyer-sub">という選択</p>
  <p class="vertical catch-body buyer-body">設備の整った店舗を少ない費用で。<br>独立への一歩を、確かな形に。<br>歴史あるお店を引き継ぎます。</p>

  <div class="free-badge">査定<br>無料</div>
  <h1 class="lead-title">大事なお店、最も高く売却いたします。</h1>
  <p class="lead-text">通常の閉店と比較して、造作を売却することで費用を抑え、利益を得ることができます。<br>神奈川エリアに特化した唯一のエージェントが、売る方・買う方の双方をサポートします。</p>

  <section class="sim sim-exit">
    <h3 class="sim-title">退店コストシミュレーション</h3>
    <table>
      <thead><tr><th></th><th>通常閉店</th><th class="own">弊社サービス</th></tr></thead>
      <tbody>
        <tr><th>解約前予告家賃</th><td>▲450,000円</td><td class="own">0円</td></tr>
        <tr><th>内装解体費用</th><td>▲550,000円</td><td class="own">0円</td></tr>
        <tr><th>造作売買代金</th><td>0円</td><td class="own">2,000,000円</td></tr>
        <tr class="total"><th>計</th><td>▲1,000,000円</td><td class="own">2,000,000円</td></tr>
      </tbody>
    </table>
    <div class="sim-merit">3,000,000円<small>のメリット</small></div>
  </section>

  <section class="sim sim-open">
    <h3 class="sim-title">出店コストシミュレーション</h3>
    <table>
      <thead><tr><th></th><th>通常出店</th><th class="own">弊社サービス</th></tr></thead>
      <tbody>
        <tr><th>内装設備投資</th><td>13,000,000円</td><td class="own">0円</td></tr>
        <tr><th>造作売買代金</th><td>0円</td><td class="own">3,700,000円</td></tr>
        <tr><th>仲介手数料</th><td>0円</td><td class="own">0円</td></tr>
        <tr class="total"><th>計</th><td>13,000,000円</td><td class="own">3,700,000円</td></tr>
      </tbody>
    </table>
    <div class="sim-merit">9,300,000円<small>のメリット</small></div>
  </section>

  <footer class="footer">
    <div class="brand">
      <p class="brand-note">神奈川エリアに特化した<br>唯一のエージェントです</p>
      <p class="brand-name"><span class="brand-mark"></span>VELKO HARBORS</p>
      <p class="brand-kana">ヴェルコハーバーズ</p>
    </div>

    <div class="contact">
      <p class="contact-lead">
        <svg width="13" height="13" viewBox="0 0 24 24" aria-hidden="true"><path d="M6.6 10.8a15.1 15.1 0 0 0 6.6 6.6l2.2-2.2a1 1 0 0 1 1-.25 11.4 11.4 0 0 0 3.6.57 1 1 0 0 1 1 1V20a1 1 0 0 1-1 1A17 17 0 0 1 3 4a1 1 0 0 1 1-1h3.5a1 1 0 0 1 1 1c0 1.25.2 2.45.57 3.57a1 1 0 0 1-.25 1z" fill="#1d3556"/></svg>
        お気軽にご相談ください
      </p>
      <p class="contact-tel">0120-471-362</p>
      <p class="contact-addr">受付 10:00〜19:00（土日祝除く）　神奈川県横浜市中区海岸通1-2-3 ハーバービル5F</p>
    </div>

    <div class="web">
      <p class="web-lead">詳しくはWebで検索</p>
      <p class="web-url">www.velko-harbors-jp.example</p>
      <div class="search">
        <span class="search-field">ヴェルコハーバーズ</span>
        <span class="search-button">検索</span>
      </div>
    </div>
  </footer>

</main>
</body>
</html>
```